Three Ebook Covers for Short Stories

Three Ebook cover designs for 3 short stories (all linked) psychological thriller. I like clean crisp images. Perhaps with an imagine of eyes/part of face - white woman, 29, thin, brown eyes, short bob hair. I like gritty, moody, raw type of images. I dont mind the same image being used on three covers providing there are differences (ie slight variation in colour of book). Colours I prefer red, burgundy, black, grey, white. My website shows off the type of colours I prefer. www.lydiakbarnes-author.net
Branding is important.

Target Market(s)

Adult. Moth in Attic, Lost Field, type of readers.

Industry/Entity Type

Book Publisher

Font styles to use
Sans Serif
Other font styles liked:
• fonts used on thriller novels

Requirements
Must have
• Author Name: Lydia K Barnes
• Short Story as Part of Title
• Short Story 1: Title - First Crow
• Short Story 2: Title - Second Crow
• Short Story 3: Title - Third Crow
• Branding is important so they must look like they are a set.
• A font which is aligned to thriller type novels
• Colours aligned to my website - red, burgundy, white, grey, black.
Nice to have
• I don't mind a black and white type photo imagine.
Should not have
• n/a

```html
<!DOCTYPE html>
<html lang="en">
<head>
<meta charset="UTF-8">
<title>First Crow — Lydia K Barnes</title>
<link rel="stylesheet" href="https://fonts.googleapis.com/css2?family=Anton&family=Oswald:wght@600&family=Roboto:wght@700&display=swap">
<style>
  :root {
    --fog-light: #c3c5bc;
    --fog-mid: #8c8e86;
    --fog-dark: #2a2b27;
    --paper: #f4f1ee;
    --eyes-deep: #5e0f24;
    --eyes-mid: #b0365a;
    --eyes-light: #e07a98;
    --title: #4b0a0c;
    --author: #b6b5a6;
    --number: #111111;
  }
  html, body {
    margin: 0;
    padding: 0;
    overflow: hidden;
    background: #ffffff;
  }
  .cover {
    position: relative;
    width: 800px;
    height: 1200px;
    overflow: hidden;
    background: linear-gradient(180deg, var(--fog-light) 0%, #aeb0a7 30%, var(--fog-mid) 58%, #4a4b45 80%, var(--fog-dark) 100%);
  }
  .fog-scene {
    position: absolute;
    inset: 0;
    background: radial-gradient(ellipse 60% 40% at 80% 65%, rgba(40,42,36,0.35), transparent 70%),
                radial-gradient(ellipse 90% 30% at 40% 95%, rgba(20,20,18,0.45), transparent 70%);
  }
  .torn-strip {
    position: absolute;
    left: 0;
    top: 0;
    width: 800px;
    height: 1200px;
  }
  .series-number {
    position: absolute;
    left: 12px;
    top: 10px;
    margin: 0;
    font-family: "Roboto", sans-serif;
    font-weight: 700;
    font-size: 26px;
    color: var(--number);
  }
  .title {
    margin: 0;
    font-family: "Anton", sans-serif;
    font-weight: 400;
    color: var(--title);
    font-size: 116px;
    line-height: 1;
    letter-spacing: 14px;
    text-transform: uppercase;
  }
  .title-line {
    position: absolute;
    display: block;
  }
  .title-line--first { left: 50px; top: 494px; }
  .title-line--second { left: 254px; top: 584px; }
  .author {
    position: absolute;
    right: 14px;
    bottom: 10px;
    margin: 0;
    font-family: "Oswald", sans-serif;
    font-weight: 600;
    font-size: 34px;
    font-variant: small-caps;
    letter-spacing: 4px;
    color: var(--author);
  }
</style>
</head>
<body>
<div class="cover">
  <div class="fog-scene" role="img" aria-label="Misty forest with dark trees fading into fog"></div>

  <svg class="torn-strip" viewBox="0 0 800 1200" xmlns="http://www.w3.org/2000/svg">
    <defs>
      <linearGradient id="eyes-tone" x1="0" y1="0" x2="1" y2="0">
        <stop offset="0" stop-color="var(--eyes-mid)"/>
        <stop offset="0.25" stop-color="var(--eyes-deep)"/>
        <stop offset="0.5" stop-color="var(--eyes-light)"/>
        <stop offset="0.75" stop-color="var(--eyes-deep)"/>
        <stop offset="1" stop-color="var(--eyes-mid)"/>
      </linearGradient>
    </defs>
    <polygon class="paper-edge" fill="var(--paper)"
      points="0,250 40,246 90,240 140,236 190,230 240,232 290,236 340,238 390,236 440,232 470,236 500,240 540,236 580,226 610,212 630,214 650,222 680,228 720,224 750,218 780,214 800,212
              800,452 770,456 740,462 700,458 660,462 620,466 580,462 540,466 500,470 460,466 420,456 380,444 340,440 300,446 260,452 220,458 180,462 140,468 100,472 60,474 30,476 0,478"/>
    <polygon class="eye-band" fill="url(#eyes-tone)" role="img" aria-label="Close-up photograph of a woman's eyes in red tones"
      points="0,262 40,258 90,252 140,248 190,242 240,244 290,248 340,250 390,248 440,244 470,248 500,252 540,248 580,238 610,226 630,228 650,234 680,240 720,236 750,230 780,226 800,226
              800,440 770,444 740,450 700,446 660,450 620,454 580,450 540,454 500,458 460,454 420,444 380,434 340,430 300,434 260,440 220,446 180,450 140,456 100,460 60,462 30,462 0,464"/>
  </svg>

  <p class="series-number">1.</p>

  <h1 class="title">
    <span class="title-line title-line--first">First</span>
    <span class="title-line title-line--second">Crow</span>
  </h1>

  <p class="author">Lydia K Barnes</p>
</div>
</body>
</html>
```